PowerPoint Template for Consultancy Company.

We need a Power Point template for a Consultancy company based in Copenhagen, Denmark. We focus on supporting people and small companies in starting up next generation technology companies. Company name is "Vorbek-Halstrup Consulting". The template shall demonstrate growth, agility, next generation technology and following your dreams. Please include the uploaded logo.
Updates
Hi guys,
thanks for helping me on this project.
I like the font "Good Times" that is being used in my logo. I will like this to be used as minimum in the headlines in my power point template. I am not sure if it will work on standard text - but will relay on your judgement.
Kind regards
Torvald
Colors
Designer to choose colors to be used in the design.
Look and feel
Each slider illustrates characteristics of the customer's brand and the style your logo design should communicate.

```html
<!DOCTYPE html>
<html lang="en">
<head>
<meta charset="utf-8">
<title>Vorbek-Halstrup Consulting – Business Sales Pitch Presentation</title>
<link rel="stylesheet" href="https://fonts.googleapis.com/css2?family=Michroma&family=Archivo+Black&family=Barlow+Semi+Condensed:wght@400;500;600&display=swap">
<style>
:root{
  --navy:#262a6e;
  --periwinkle:#6c6f9f;
  --red:#dd3030;
  --ink:#222;
  --muted:#666;
  --paper:#f3f3f3;
  --white:#fff;
  --concrete-a:#e4e3df;
  --concrete-b:#c9c8c3;
  --photo-dark-a:#4a3a2e;
  --photo-dark-b:#9a8f86;
}
*{margin:0;padding:0;box-sizing:border-box}
html,body{width:1200px;height:2201px;overflow:hidden;background:var(--white)}
body{position:relative;font-family:"Barlow Semi Condensed",Arial,sans-serif;color:var(--ink)}
.headline{font-family:"Michroma",Arial,sans-serif;text-transform:uppercase}

/* title slide */
.cover{position:absolute;left:215px;top:73px;width:704px;height:396px;overflow:hidden}
.cover-brand{position:absolute;right:32px;top:250px;text-align:right}
.cover-name{font-family:"Michroma",sans-serif;color:var(--navy);font-size:22px;line-height:1.2}
.cover-sub{font-family:"Barlow Semi Condensed",sans-serif;font-weight:500;color:var(--red);font-size:17px;margin-top:14px;text-transform:uppercase}
.cover-tag{font-family:"Barlow Semi Condensed",sans-serif;color:var(--red);font-size:14px;margin-top:6px}

/* feature lists */
.features{position:absolute;top:557px;font-family:"Archivo Black",Arial,sans-serif;font-size:21px;line-height:30px;color:#111}
.features.left{left:104px}
.features.right{left:623px}
.features li{list-style:none;position:relative;padding-left:24px}
.features li.box::before{content:"";position:absolute;left:0;top:5px;width:19px;height:19px;border:2px solid #111;border-radius:2px}
.features ul.sub{margin-left:34px}
.features ul.sub li{padding-left:20px;line-height:27px}
.features ul.sub li::before{content:"";position:absolute;left:2px;top:8px;width:7px;height:7px;background:#111}

/* slide grid */
.slide{position:absolute;width:377px;height:214px;overflow:hidden;background:var(--paper);
  box-shadow:3px 3px 6px rgba(0,0,0,.35)}
.photo{position:absolute}
.photo.concrete{background:linear-gradient(135deg,var(--concrete-a),var(--concrete-b))}
.photo.desk{background:linear-gradient(160deg,#d8d4cf 0%,var(--photo-dark-b) 55%,var(--photo-dark-a) 100%)}
.photo.laptop{background:linear-gradient(150deg,#6b4a36 0%,#3b3b3e 55%,#1c1c1e 100%)}
.photo.stairs{background:radial-gradient(circle at 45% 55%,#5d6b4a 0 10%,#b7b2b9 24%,#8b86a0 60%,#e4e2e8 100%)}
.brand-tag{position:absolute;top:12px;right:14px;font-family:"Michroma",sans-serif;font-size:4.4px;line-height:6px;color:var(--navy);white-space:nowrap}
.brand-tag.left{left:14px;right:auto}
.title{position:absolute;left:0;right:0;top:14px;text-align:center;font-family:"Michroma",sans-serif;font-size:9.5px;text-transform:uppercase;color:#222}
.txt{font-size:5.3px;line-height:6.3px;color:var(--muted)}
.h-sm{font-family:"Michroma",sans-serif;font-size:7.5px;line-height:8.5px;text-transform:uppercase;color:#222}
.panel{position:absolute;border-radius:18px}
.icon{display:block;margin:0 auto 3px;width:16px;height:16px;background:#6c6c6c;border-radius:3px}
.social{width:10px;height:10px;border:.8px solid #777;border-radius:50%}
</style>
</head>
<body>

<section class="cover" aria-label="Title slide">
  <div class="photo" role="img" aria-label="Muted black and white photo of an open-plan office with people at desks" style="inset:0;background:linear-gradient(180deg,#d6d6d6,#a9a9a9 60%,#8a8a8a)"></div>
  <div class="cover-brand">
    <div class="cover-name">VORBEK-HALSTRUP CONSULTING</div>
    <div class="cover-sub">Management Consulting</div>
    <div class="cover-tag">Business Sales Pitch Presentation</div>
  </div>
</section>

<ul class="features left">
  <li class="box">Ratio 16:9</li>
  <li class="box">Full HD</li>
  <li class="box">Custom color pallet</li>
  <li class="box">Custom Font -&nbsp; Easy Change</li>
  <li class="box">Easy to edit, just drag and drop<br>images</li>
</ul>
<ul class="features right">
  <li class="box">Can be included up to 100&nbsp; slides;</li>
  <ul class="sub">
    <li>Text + images (1,2,3,4) , Text<br>Slides</li>
    <li>Portfolio Slides , blog slides</li>
    <li>Text Slides, infographics</li>
    <li>Data Slides</li>
  </ul>
  <li class="box">In the sample you find 22 slides</li>
</ul>

<!-- row 1 -->
<article class="slide agenda" style="left:14px;top:801px">
  <div class="photo concrete" role="img" aria-label="Photo of a white concrete stairway" style="left:12px;top:10px;width:354px;height:194px"></div>
  <div class="panel" style="left:130px;top:10px;width:236px;height:170px;background:rgba(243,243,243,.93);border-radius:22px 0 0 22px"></div>
  <div class="brand-tag">VORBEK-HALSTRUP CONSULTING</div>
  <div style="position:absolute;left:178px;top:38px;width:180px;display:grid;grid-template-columns:1fr 1fr;row-gap:14px;text-align:center">
    <div><div class="h-sm">01</div><div class="h-sm" style="font-size:5.5px;line-height:6.5px">Problem &amp;<br>Solution</div><div class="txt">Here you could describe the<br>topic of the section</div></div>
    <div><div class="h-sm">02</div><div class="h-sm" style="font-size:5.5px;line-height:6.5px">Market Analysis<br>&amp; Target</div><div class="txt">Here you could describe the<br>topic of the section</div></div>
    <div><div class="h-sm">03</div><div class="h-sm" style="font-size:5.5px;line-height:6.5px">Our<br>Process</div><div class="txt">Here you could describe the<br>topic of the section</div></div>
    <div><div class="h-sm">04</div><div class="h-sm" style="font-size:5.5px;line-height:6.5px">Our<br>Consultants</div><div class="txt">Here you could describe the<br>topic of the section</div></div>
  </div>
</article>

<article class="slide company" style="left:413px;top:801px">
  <div class="photo desk" role="img" aria-label="Photo of hands writing on paper at a wooden table" style="left:12px;top:10px;width:354px;height:194px"></div>
  <div class="panel" style="left:12px;top:10px;width:236px;height:154px;background:rgba(240,240,240,.94);border-radius:0 0 22px 0"></div>
  <div class="brand-tag left" style="top:16px">VORBEK-HALSTRUP CONSULTING</div>
  <div class="h-sm" style="position:absolute;left:43px;top:55px;font-size:8px;line-height:10px">Our<br>Company</div>
  <div class="txt" style="position:absolute;left:43px;top:77px;width:128px">Mercury is the closest planet to the Sun and the smallest one in the Solar System—it's only a bit larger than our Moon. The planet's name has nothing to do with the liquid metal, since it was named after the Roman messenger god, Mercury</div>
</article>

<article class="slide what-we-do" style="left:812px;top:801px">
  <div class="photo concrete" role="img" aria-label="Photo of a curved white stairway" style="left:0;top:29px;width:188px;height:185px;border-radius:0 24px 0 0"></div>
  <div class="brand-tag">VORBEK-HALSTRUP CONSULTING</div>
  <div class="title" style="left:190px;top:47px">What we do</div>
  <div class="txt" style="position:absolute;left:200px;top:62px;width:170px;text-align:center;font-size:6px;color:#333">Lorem ipsum dolor sit amet consectetur adipiscing elit id tortor, aliquet sapien massa litora malesuada cum</div>
  <div style="position:absolute;left:146px;top:89px;width:104px;height:82px;background:#fff;border-radius:10px 10px 0 10px;box-shadow:2px 2px 4px rgba(0,0,0,.3);padding:14px 10px 0 24px">
    <ul class="txt" style="font-size:4.6px;line-height:5.4px"><li>Lorem ipsum dolor sit amet consectetur adipiscing elit id tortor, aliquet sapien massa litora malesuada cum</li><li style="margin-top:4px">Lorem ipsum dolor sit amet consectetur adipiscing elit id tortor, aliquet sapien massa litora malesuada cum</li></ul>
  </div>
  <div style="position:absolute;left:257px;top:89px;width:104px;height:82px;background:#fff;border-radius:10px 10px 0 10px;box-shadow:2px 2px 4px rgba(0,0,0,.3);padding:14px 10px 0 24px">
    <ul class="txt" style="font-size:4.6px;line-height:5.4px"><li>Lorem ipsum dolor sit amet consectetur adipiscing elit id tortor, aliquet sapien massa litora malesuada cum</li><li style="margin-top:4px">Lorem ipsum dolor sit amet consectetur adipiscing elit id tortor, aliquet sapien massa litora malesuada cum</li></ul>
  </div>
</article>

<!-- row 2 -->
<article class="slide section-01" style="left:14px;top:1063px">
  <div class="photo concrete" role="img" aria-label="Photo of a concrete stairwell with a black handrail" style="left:12px;top:10px;width:354px;height:194px"></div>
  <div class="panel" style="left:190px;top:0;width:187px;height:162px;background:var(--paper);border-radius:24px 0 0 24px"></div>
  <div class="brand-tag">VORBEK-HALSTRUP CONSULTING</div>
  <div class="headline" style="position:absolute;right:58px;top:92px;text-align:right;font-size:16px;line-height:21px">01<br>Section</div>
  <div class="txt" style="position:absolute;left:210px;top:139px;font-size:5px">You could enter a subtitle here if you need it</div>
</article>

<article class="slide problems" style="left:413px;top:1063px">
  <div class="brand-tag">VORBEK-HALSTRUP CONSULTING</div>
  <div class="title" style="right:110px;top:17px;font-size:8.5px">Understanding the problem</div>
  <div class="photo stairs" role="img" aria-label="Photo looking down a spiral staircase" style="left:0;top:45px;width:255px;height:159px"></div>
  <div style="position:absolute;left:255px;top:45px;width:122px;height:159px;background:var(--navy)"></div>
  <div style="position:absolute;left:44px;top:112px;width:72px"><div class="h-sm" style="color:#fff;font-size:5.5px">Problem 1</div><div class="txt" style="color:#eee">Despite being red, Mars is actually a cold place. It's full of iron oxide dust, which gives the planet its reddish cast</div></div>
  <div style="position:absolute;left:154px;top:112px;width:72px"><div class="h-sm" style="color:#fff;font-size:5.5px">Problem 2</div><div class="txt" style="color:#eee">It's a gas giant and the biggest planet in our Solar System. Jupiter is the fourth-brightest object in the sky</div></div>
  <div style="position:absolute;left:265px;top:112px;width:90px"><div class="h-sm" style="color:#fff;font-size:5.5px">Problem 3</div><div class="txt" style="color:#eee">as a beautiful name and is the second planet from the Sun. It's terribly hot, even hotter than others</div></div>
</article>

<article class="slide problem-1" style="left:812px;top:1063px">
  <div class="photo laptop" role="img" aria-label="Photo of a laptop showing a data dashboard" style="left:0;top:29px;width:188px;height:185px;border-radius:0 24px 0 0"></div>
  <div class="brand-tag">VORBEK-HALSTRUP CONSULTING</div>
  <div class="h-sm" style="position:absolute;left:207px;top:50px;font-size:8px">Problem 1</div>
  <ul class="txt" style="position:absolute;left:225px;top:77px;width:135px;font-size:4.6px;line-height:5.3px">
    <li>Despite being red, Mars is actually a cold place. It's full of iron oxide dust, which gives the planet its reddish cast</li>
    <li>Despite being red, Mars is actually a cold place. It's full of iron oxide dust, which gives the planet its reddish cast</li>
    <li>Despite being red, Mars is actually a cold place. It's full of iron oxide dust, which gives the planet its reddish cast</li>
    <li>Despite being red, Mars is actually a cold place. It's full of iron oxide dust, which gives the planet its reddish cast</li>
    <li>Despite being red, Mars is actually a cold place. It's full of iron oxide dust, which gives the planet its reddish cast</li>
    <li>Despite being red, Mars is actually a cold place. It's full of iron oxide dust, which gives the planet its reddish cast</li>
  </ul>
</article>

<!-- row 3 -->
<article class="slide solutions" style="left:14px;top:1326px">
  <div class="brand-tag">VORBEK-HALSTRUP CONSULTING</div>
  <div class="title" style="right:110px;top:18px;font-size:8.5px">Our solutions</div>
  <div class="panel" style="left:0;top:49px;width:365px;height:157px;background:var(--periwinkle);border-radius:0 22px 22px 0"></div>
  <div style="position:absolute;left:30px;top:84px;width:310px;display:grid;grid-template-columns:1fr 1fr;row-gap:20px;text-align:center">
    <div><div class="h-sm" style="color:#fff;font-size:5.5px">Solution 1</div><div class="txt" style="color:#f1f1f1">Venus has a beautiful name and is the second planet<br>from the Sun. It's terribly hot</div></div>
    <div><div class="h-sm" style="color:#fff;font-size:5.5px">Solution 2</div><div class="txt" style="color:#f1f1f1">Saturn is the ringed one. It's a gas giant, composed<br>mostly of hydrogen and helium</div></div>
    <div><div class="h-sm" style="color:#fff;font-size:5.5px">Solution 3</div><div class="txt" style="color:#f1f1f1">Mercury is the closest planet to the Sun and the<br>smallest one in our Solar System</div></div>
    <div><div class="h-sm" style="color:#fff;font-size:5.5px">Solution 4</div><div class="txt" style="color:#f1f1f1">Neptune is the farthest planet from the Sun and the<br>fourth-largest in our Solar System</div></div>
  </div>
</article>

<article class="slide break" style="left:413px;top:1326px">
  <div class="photo concrete" role="img" aria-label="Photo of a curved white concrete stairway" style="left:12px;top:10px;width:354px;height:194px;border-radius:0 0 22px 22px"></div>
  <div class="headline" style="position:absolute;left:0;right:0;top:98px;text-align:center;font-size:17px;color:rgba(255,255,255,.85)">Break section</div>
</article>

<article class="slide numbers" style="left:812px;top:1326px">
  <div class="brand-tag">VORBEK-HALSTRUP CONSULTING</div>
  <div class="title" style="right:110px;top:18px;font-size:8.5px">Main numbers</div>
  <div style="position:absolute;left:12px;top:45px;width:354px;height:161px;background:#e6e6e9"></div>
  <svg style="position:absolute;left:12px;top:45px" width="354" height="161" viewBox="0 0 354 161" aria-label="Bar chart of four series across four categories">
    <g font-family="Barlow Semi Condensed,sans-serif" font-size="6" fill="#444" text-anchor="end">
      <text x="53" y="143">0</text><text x="53" y="132">0.5</text><text x="53" y="122">1</text><text x="53" y="111">1.5</text><text x="53" y="101">2</text><text x="53" y="90">2.5</text><text x="53" y="80">3</text><text x="53" y="69">3.5</text><text x="53" y="59">4</text><text x="53" y="48">4.5</text><text x="53" y="38">5</text>
    </g>
    <g>
      <rect x="70" y="53" width="13" height="88" fill="#252b73"/><rect x="83" y="91" width="13" height="50" fill="#e1352f"/><rect x="96" y="101" width="13" height="40" fill="#e1352f"/><rect x="109" y="97" width="13" height="44" fill="#2f5fd6"/>
      <rect x="128" y="91" width="13" height="50" fill="#252b73"/><rect x="141" y="50" width="13" height="91" fill="#e1352f"/><rect x="154" y="55" width="13" height="86" fill="#e1352f"/><rect x="167" y="97" width="13" height="44" fill="#2f5fd6"/>
      <rect x="186" y="68" width="13" height="73" fill="#252b73"/><rect x="199" y="101" width="13" height="40" fill="#e1352f"/><rect x="212" y="107" width="13" height="34" fill="#e1352f"/><rect x="225" y="78" width="13" height="63" fill="#2f5fd6"/>
      <rect x="244" y="49" width="13" height="92" fill="#252b73"/><rect x="257" y="83" width="13" height="58" fill="#e1352f"/><rect x="270" y="97" width="13" height="44" fill="#e1352f"/><rect x="283" y="33" width="13" height="108" fill="#2f5fd6"/>
    </g>
    <g font-family="Barlow Semi Condensed,sans-serif" font-size="6" fill="#444" text-anchor="middle">
      <text x="96" y="152">Category 1</text><text x="154" y="152">Category 2</text><text x="212" y="152">Category 3</text><text x="270" y="152">Category 4</text>
    </g>
    <g font-family="Barlow Semi Condensed,sans-serif" font-size="6" fill="#444">
      <rect x="310" y="82" width="4" height="4" fill="#2f5fd6"/><text x="317" y="86">Series 1</text>
      <rect x="310" y="92" width="4" height="4" fill="#e1352f"/><text x="317" y="96">Series 2</text>
      <rect x="310" y="102" width="4" height="4" fill="#e1352f"/><text x="317" y="106">Series 3</text>
      <rect x="310" y="112" width="4" height="4" fill="#252b73"/><text x="317" y="116">Series 4</text>
    </g>
  </svg>
</article>

<!-- row 4 -->
<article class="slide section-02" style="left:14px;top:1589px">
  <div class="photo concrete" role="img" aria-label="Photo of a concrete stairwell with a black handrail" style="left:12px;top:10px;width:354px;height:194px"></div>
  <div class="panel" style="left:190px;top:0;width:187px;height:162px;background:var(--paper);border-radius:24px 0 0 24px"></div>
  <div class="brand-tag">VORBEK-HALSTRUP CONSULTING</div>
  <div class="headline" style="position:absolute;right:58px;top:92px;text-align:right;font-size:16px;line-height:21px">02<br>Section</div>
  <div class="txt" style="position:absolute;left:210px;top:139px;font-size:5px">You could enter a subtitle here if you need it</div>
</article>

<article class="slide analysis-values" style="left:413px;top:1589px">
  <div class="brand-tag">VORBEK-HALSTRUP CONSULTING</div>
  <div class="title" style="top:18px;font-size:8.5px">Analysis</div>
  <div class="panel" style="left:12px;top:38px;width:365px;height:158px;background:var(--navy);border-radius:22px 0 0 22px"></div>
  <svg style="position:absolute;left:12px;top:38px" width="365" height="158" viewBox="0 0 365 158" aria-label="Concentric ring chart of top rated values">
    <text x="20" y="22" font-family="Barlow Semi Condensed,sans-serif" font-size="6" fill="#d8d9ee">TOP RATED VALUES</text>
    <g fill="none" stroke="#fff" stroke-width="5">
      <circle cx="68" cy="88" r="60" stroke="#8d8fb8"/>
      <path d="M68 28 A60 60 0 1 1 8 88"/>
      <circle cx="68" cy="88" r="40" stroke="#8d8fb8"/>
      <path d="M68 48 A40 40 0 1 1 28 88"/>
      <circle cx="68" cy="88" r="22"/>
    </g>
    <g stroke="#fff" stroke-width=".8"><line x1="68" y1="28" x2="245" y2="28"/><line x1="68" y1="48" x2="245" y2="48"/><line x1="68" y1="66" x2="245" y2="66"/></g>
    <g fill="none" stroke="#fff" stroke-width=".8"><rect x="252" y="23" width="9" height="9"/><circle cx="256" cy="47" r="5"/><circle cx="256" cy="65" r="5"/></g>
    <g font-family="Barlow Semi Condensed,sans-serif" font-size="6.5" fill="#fff"><text x="268" y="31">20%</text><text x="268" y="50">50%</text><text x="268" y="68">24%</text></g>
    <text x="255" y="135" text-anchor="middle" font-family="Michroma,sans-serif" font-size="7" fill="#fff">15,000,000</text>
    <text x="255" y="147" text-anchor="middle" font-family="Barlow Semi Condensed,sans-serif" font-size="5" fill="#d8d9ee">Worldwide clients</text>
  </svg>
</article>

<article class="slide infographic" style="left:812px;top:1589px">
  <div class="brand-tag">VORBEK-HALSTRUP CONSULTING</div>
  <div class="title" style="top:18px;font-size:8.5px">Infographic</div>
  <div class="panel" style="left:12px;top:38px;width:365px;height:158px;background:var(--navy);border-radius:22px 0 0 22px"></div>
  <svg style="position:absolute;left:60px;top:62px" width="130" height="120" viewBox="0 0 130 120" aria-label="Three-step cycle of arrows">
    <g fill="none" stroke-width="15">
      <path d="M20 78 A46 46 0 0 1 52 16" stroke="#c9cbef"/>
      <path d="M78 16 A46 46 0 0 1 106 78" stroke="#6fb3e0"/>
      <path d="M96 96 A46 46 0 0 1 30 96" stroke="#e0282b"/>
    </g>
    <polygon points="50,3 68,17 50,30" fill="#c9cbef"/>
    <polygon points="94,76 118,76 106,94" fill="#6fb3e0"/>
    <polygon points="34,84 34,110 18,97" fill="#e0282b"/>
  </svg>
  <div style="position:absolute;left:226px;top:70px;width:130px">
    <div class="h-sm" style="color:#fff;font-size:5.5px">Step 1</div><div class="txt" style="color:#e6e6f2">Venus has a beautiful name and is the second planet from the Sun. It's terribly hot</div>
    <div class="h-sm" style="color:#fff;font-size:5.5px;margin-top:10px">Step 2</div><div class="txt" style="color:#e6e6f2">Saturn is the ringed one. It's a gas giant, composed mostly of hydrogen and helium</div>
    <div class="h-sm" style="color:#fff;font-size:5.5px;margin-top:10px">Step 3</div><div class="txt" style="color:#e6e6f2">Mercury is the closest planet to the Sun and the smallest one in our Solar System</div>
  </div>
</article>

<!-- row 5 -->
<article class="slide analysis-outreach" style="left:14px;top:1851px">
  <div class="title" style="top:20px;font-size:8.5px">Analysis</div>
  <div class="panel" style="left:0;top:45px;width:365px;height:159px;background:var(--periwinkle);border-radius:0 22px 22px 0"></div>
  <div class="txt" style="position:absolute;left:33px;top:58px;color:#e4e4f0">OUTREACH</div>
  <div role="img" aria-label="Dotted world map showing outreach regions" style="position:absolute;left:12px;top:70px;width:230px;height:118px;background:radial-gradient(ellipse at 50% 45%,rgba(255,255,255,.35),rgba(255,255,255,.08) 70%);border-radius:8px"></div>
  <svg style="position:absolute;left:0;top:45px" width="365" height="159" viewBox="0 0 365 159" aria-hidden="true">
    <g stroke="#fff" stroke-width=".8"><line x1="195" y1="27" x2="265" y2="27"/><line x1="137" y1="73" x2="265" y2="73"/><line x1="72" y1="125" x2="265" y2="125"/></g>
    <g fill="#fff" fill-opacity=".6" stroke="#fff"><circle cx="195" cy="27" r="7"/><circle cx="137" cy="73" r="7"/><circle cx="72" cy="125" r="7"/></g>
  </svg>
  <div style="position:absolute;left:270px;top:64px;color:#fff">
    <div class="headline" style="font-size:9px">1,520</div><div class="txt" style="color:#eee;width:75px">Saturn is a gas giant, composed mostly of hydrogen and helium</div>
    <div class="headline" style="font-size:9px;margin-top:14px">5,000</div><div class="txt" style="color:#eee;width:75px">Jupiter is the biggest planet in our Solar System</div>
    <div class="headline" style="font-size:9px;margin-top:16px">3,250</div><div class="txt" style="color:#eee;width:75px">Neptune is the farthest planet from the Sun</div>
  </div>
</article>

<article class="slide target" style="left:413px;top:1851px">
  <div class="brand-tag">VORBEK-HALSTRUP CONSULTING</div>
  <div class="title" style="top:18px;font-size:8.5px">Target</div>
  <div class="photo desk" role="img" aria-label="Photo of two people talking at a wooden table" style="left:12px;top:45px;width:117px;height:158px;border-radius:0 0 0 18px"></div>
  <div class="photo" role="img" aria-label="Photo of a desktop computer on an office desk" style="left:247px;top:45px;width:118px;height:158px;border-radius:18px 0 0 0;background:linear-gradient(160deg,#d9c7a6,#6d7f98 50%,#2b3343)"></div>
  <div style="position:absolute;left:140px;top:60px;width:98px;display:grid;grid-template-columns:1fr 1fr;row-gap:9px;text-align:center">
    <div><i class="icon"></i><span class="txt" style="font-size:4.5px">REAL ESTATE</span></div>
    <div><i class="icon"></i><span class="txt" style="font-size:4.5px">AUTOMOTIVE</span></div>
    <div><i class="icon"></i><span class="txt" style="font-size:4.5px">TECHNOLOGY</span></div>
    <div><i class="icon"></i><span class="txt" style="font-size:4.5px">INSURANCE</span></div>
    <div><i class="icon"></i><span class="txt" style="font-size:4.5px">RETAIL</span></div>
    <div><i class="icon"></i><span class="txt" style="font-size:4.5px">ENERGY</span></div>
  </div>
  <div style="position:absolute;left:150px;top:181px;width:78px;border-top:.8px solid #777"></div>
  <div class="h-sm" style="position:absolute;left:140px;width:98px;top:185px;text-align:center;font-size:5px">Clients</div>
</article>

<article class="slide thanks" style="left:812px;top:1851px">
  <div class="photo" role="img" aria-label="Photo of a white staircase with metal railings" style="left:12px;top:10px;width:354px;height:116px;border-radius:0 0 18px 18px;background:linear-gradient(135deg,#9c9c9c,#e6e6e6 60%,#cfcfcf)"></div>
  <div class="headline" style="position:absolute;left:0;right:0;top:134px;text-align:center;font-size:10px">Thanks!</div>
  <div class="txt" style="position:absolute;left:30px;top:149px;font-size:6.2px;color:#444">Does anyone have any questions?</div>
  <div class="txt" style="position:absolute;left:30px;top:165px;font-size:4.8px;line-height:6.4px;color:#444">youremail@vorbek-halstrup.com<br>+45 31 72 90 14<br>yourcompany.com</div>
  <div style="position:absolute;left:290px;top:148px;display:flex;gap:4px">
    <i class="social"></i><i class="social"></i><i class="social"></i><i class="social"></i>
  </div>
</article>

</body>
</html>
```